Kickbut Home Page Design built to Sell

We need a new home page layout. The website is working now but we need a refresh. Our business has slowed down since a few years ago. We need to show we build ecommerce and membership websites. Here is the page now: https://www.qelvartinbuild.graphics/new-home/

Target Market(s)

Women, solopreneurs, artists, politicians

Industry/Entity Type

Design Agency

Number of Pages Required

1 page

Font styles to use
Sans Serif

Colors
b8a6cd
fabb94
acd136
00a990

Requirements
Must have
• Video header
Section for text and Step process similar to this website: https://tovarellaplexworks.com/ [This is out sister company]
Places for images.
Call to action lead gen form and Get a quote.
The menu should show WEB, PRINT, VIDEO
Nice to have
• I LOVE this company: https://plumeravik.com/guide/
Area for testimonials
Should not have
• We don't want a duplicate of https://tovarellaplexworks.com/

```html
<!DOCTYPE html>
<html lang="en">
<head>
<meta charset="utf-8">
<title>Qelvartin Build — Lead Generating Websites</title>
<link href="https://fonts.googleapis.com/css2?family=Montserrat:wght@400;500;600;700;800&family=Roboto+Condensed:wght@400&display=swap" rel="stylesheet">
<style>
:root{
  --lavender:#b8a6cd;
  --purple:#7e5cc4;
  --deep-purple:#6a4bc0;
  --peach:#fabb94;
  --lime:#acd136;
  --teal:#00a990;
  --ink:#2b2b3a;
  --muted:#6b6b78;
  --soft:#f2f2f4;
  --night:#2c1b4c;
  --white:#ffffff;
}
*{box-sizing:border-box;margin:0;padding:0}
html,body{width:1200px;height:4773px;overflow:hidden}
body{font-family:"Montserrat",sans-serif;color:var(--ink);background:var(--white);position:relative}
.abs{position:absolute}
.btn{position:absolute;display:flex;align-items:center;justify-content:center;border-radius:30px;font-weight:700;font-size:13px;letter-spacing:.5px;text-transform:uppercase}
.btn-lime{background:var(--lime);color:var(--white)}
.btn-teal{background:var(--teal);color:var(--white)}
.btn-outline-teal{border:2px solid var(--teal);color:var(--teal);background:var(--white)}

/* Hero */
.hero{position:absolute;left:0;top:0;width:1200px;height:760px;overflow:hidden}
.hero-photo{position:absolute;inset:0 0 60px 0;background:linear-gradient(120deg,#8a7a6c 0%,#5f5a58 40%,#9c8a7a 70%,#6b6c70 100%)}
.hero-photo::after{content:"";position:absolute;inset:0;background:rgba(40,30,40,.35)}
.logo{position:absolute;color:var(--white);font-weight:700;letter-spacing:1px;display:flex;align-items:center;gap:10px}
.logo i{display:block;width:12px;height:12px;background:currentColor}
.nav a{position:absolute;top:29px;color:var(--white);font-size:13px;text-decoration:none}
.phone{position:absolute;left:1003px;top:25px;color:var(--white);font-size:14px;font-weight:600;display:flex;align-items:center;gap:6px}
.hero h1{position:absolute;left:0;width:1200px;top:290px;text-align:center;color:var(--white);font-weight:800;font-size:37px;line-height:42px;text-transform:uppercase}
.hero h1 span{display:block;font-weight:400;font-size:31px}

/* Audit */
.audit-ring{position:absolute;left:117px;top:756px;width:452px;height:452px;border-radius:50%;background:#e2f4f1}
.audit-ring2{position:absolute;left:143px;top:782px;width:400px;height:400px;border-radius:50%;background:#8dd6c7}
.audit-photo{position:absolute;left:155px;top:794px;width:376px;height:376px;border-radius:50%;background:linear-gradient(135deg,#c99a74,#2f6f86 60%,#17374a)}
.audit h2{position:absolute;left:606px;top:838px;width:440px;font-size:24px;line-height:34px;font-weight:700}
.audit p{position:absolute;left:606px;top:962px;width:440px;font-size:16px;line-height:26px;color:var(--muted)}

/* About band */
.about{position:absolute;left:124px;top:1274px;width:978px;height:272px;background:#f2eef8;border-radius:6px;overflow:hidden}
.about h3{position:absolute;left:404px;top:64px;width:520px;font-size:17px;line-height:28px;font-weight:700}
.about p{position:absolute;left:404px;top:132px;width:520px;font-size:15px;line-height:27px;color:var(--muted)}

/* Steps */
.step{position:absolute;width:260px;text-align:center}
.step h4{font-family:"Roboto Condensed",sans-serif;font-weight:400;font-size:18px;letter-spacing:2.5px;color:var(--ink);margin-top:18px}
.step p{font-size:12px;line-height:19px;color:var(--muted);margin:14px auto 0;width:200px}
.step .ico{width:82px;height:82px;border-radius:50%;margin:0 auto;display:flex;align-items:center;justify-content:center}

/* Services */
.services h2{position:absolute;left:120px;top:2196px;font-size:30px;font-weight:700}
.services h2 span{font-weight:400}
.rule{position:absolute;height:4px;border-radius:2px;background:var(--teal)}
.services p{position:absolute;left:120px;top:2272px;width:410px;font-size:14px;line-height:28px;color:var(--muted)}
.card{position:absolute;width:226px;padding:22px 24px;font-size:10px;line-height:15px;box-shadow:0 8px 24px rgba(40,20,80,.12)}
.card h5{font-size:14px;font-weight:600;margin:12px 0 10px;letter-spacing:.3px;text-transform:uppercase}
.card .mini{display:inline-block;margin-top:12px;border-radius:12px;padding:4px 18px;font-size:7px;font-weight:700;text-transform:uppercase}
.card-teal{background:var(--teal);color:var(--white)}
.card-lime{background:var(--lime);color:var(--white)}
.card-white{background:var(--white);color:var(--ink)}
.card-white p{color:var(--muted)}

/* Testimonials */
.testi h2{position:absolute;left:0;width:1200px;top:2720px;text-align:center;font-size:30px;font-weight:700}
.testi h2 span{font-weight:400}
.testi-card{position:absolute;left:117px;top:2793px;width:933px;height:331px;background:var(--white);box-shadow:0 10px 30px rgba(0,0,0,.08)}
.testi-photo{position:absolute;left:0;top:0;width:472px;height:331px;background:linear-gradient(120deg,#c9d6e4,#7c95b4 55%,#e7ecf1)}
.play{position:absolute;left:210px;top:125px;width:56px;height:56px;border-radius:50%;background:rgba(255,255,255,.9);display:flex;align-items:center;justify-content:center}
.testi-card h3{position:absolute;left:518px;top:56px;width:380px;font-size:18px;line-height:30px;font-weight:700}
.testi-card p{position:absolute;left:518px;top:132px;width:380px;font-size:12px;line-height:20px;color:var(--muted)}

/* Projects */
.projects h2{position:absolute;left:115px;top:3374px;font-size:28px;font-weight:800;color:#3a3a48}
.projects h3{position:absolute;left:115px;top:3455px;width:300px;font-size:18px;line-height:24px;font-weight:700}
.projects p{position:absolute;left:115px;top:3522px;width:270px;font-size:13px;line-height:24px;color:var(--muted)}

/* Quote form */
.quote-bg{position:absolute;left:0;top:3856px;width:1200px;height:592px;background:linear-gradient(100deg,#c4dc5c 0%,#8fd07f 45%,#3cc2a0 100%)}
.quote-card{position:absolute;left:178px;top:3932px;width:863px;height:463px;background:var(--white);border-radius:40px 180px 40px 40px}
.quote-card h2{position:absolute;left:0;width:863px;top:50px;text-align:center;font-size:22px;font-weight:700;color:#4a4a58}
.field{position:absolute;width:333px;height:46px;border:1.5px solid #cfcfd8;border-radius:23px;font-size:11px;font-weight:500;color:#4a4a58;padding:16px 28px}
.field.msg{width:681px;height:70px;border-radius:10px;padding:10px 24px}

/* Footer */
.footer{position:absolute;left:0;top:4448px;width:1200px;height:325px;background:var(--night);color:var(--white)}
.footer h6{position:absolute;top:64px;font-size:14px;font-weight:700;letter-spacing:.5px}
.footer .small{position:absolute;font-size:12px;line-height:20px;color:#d9d3e8}
.divider{position:absolute;top:60px;width:3px;height:22px;background:var(--white)}
.vline{position:absolute;top:0;width:1px;height:325px;background:rgba(255,255,255,.12)}
</style>
</head>
<body>

<!-- HERO -->
<section class="hero">
  <div class="hero-photo" role="img" aria-label="Video header still: two colleagues reviewing work at a laptop"></div>
  <div class="logo" style="left:70px;top:22px;font-size:22px"><i></i>QELVARTIN BUILD</div>
  <div class="abs" style="left:70px;top:50px;font-size:7px;color:#fff;letter-spacing:1.2px">GRAPHICS WEB VIDEO CONSULTANTS</div>
  <nav class="nav">
    <a style="left:503px">WEB</a>
    <a style="left:611px">PRINT</a>
    <a style="left:728px">VIDEO</a>
  </nav>
  <div class="phone">
    <svg width="20" height="20" viewBox="0 0 20 20"><circle cx="10" cy="10" r="10" fill="#5cc04a"/><path d="M7 5.5l1.6 2.6-1 1c.6 1.3 1.6 2.3 2.9 2.9l1-1 2.6 1.6-.8 1.8c-3.7 0-7.2-3.5-7.2-7.2z" fill="#fff"/></svg>
    413-555-0187
  </div>
  <h1>Lead Generating Websites That<span>Move Your Business Forward</span></h1>
  <div class="btn btn-lime" style="left:407px;top:394px;width:180px;height:44px">Get a Quote</div>
  <div class="btn" style="left:596px;top:394px;width:182px;height:44px;border:2px solid #fff;color:#fff;gap:10px">
    <svg width="22" height="22" viewBox="0 0 22 22"><circle cx="11" cy="11" r="11" fill="#fff"/><path d="M9 7l6 4-6 4z" fill="#555"/></svg>Play Video
  </div>
  <svg class="abs" style="left:0;top:590px" width="1200" height="170" viewBox="0 0 1200 170" preserveAspectRatio="none">
    <path d="M0 60 C200 40 350 110 560 70 C760 30 900 0 1060 40 C1130 60 1170 80 1200 90 L1200 170 L0 170Z" fill="#1d7f6a"/>
    <path d="M0 70 C220 50 360 120 580 80 C780 40 900 20 1040 60 C1120 80 1170 100 1200 110 L1200 170 L0 170Z" fill="var(--lime)"/>
    <path d="M0 80 C180 60 380 130 600 95 C720 75 820 60 900 80 C1000 110 1100 130 1200 130 L1200 170 L0 170Z" fill="#16c5b0"/>
    <path d="M0 100 C200 90 380 150 640 120 C850 96 1000 130 1200 140 L1200 170 L0 170Z" fill="#fff"/>
  </svg>
</section>

<!-- AUDIT -->
<section class="audit">
  <div class="audit-ring"></div>
  <div class="audit-ring2"></div>
  <div class="audit-photo" role="img" aria-label="Photo: designer working with a digital data display"></div>
  <h2>How is your website performing? Discover problems with your web-site and how to solve them.</h2>
  <p>This website and SEO audit is specifically designed for businesses and organizations who are working to develop, implement or improve their website and online marketing strategy.</p>
  <div class="btn btn-outline-teal" style="left:603px;top:1100px;width:206px;height:50px">Get a Free Quote</div>
</section>

<!-- ABOUT -->
<section class="about">
  <svg class="abs" style="left:0;top:0" width="370" height="272" viewBox="0 0 370 272">
    <defs><linearGradient id="aboutGrad" x1="0" y1="0" x2="0.3" y2="1"><stop offset="0" stop-color="#b8a6cd"/><stop offset="1" stop-color="#6a4bc0"/></linearGradient></defs>
    <path d="M0 0 H290 C370 60 380 200 290 272 H0Z" fill="url(#aboutGrad)"/>
  </svg>
  <div class="logo" style="left:58px;top:110px;font-size:28px"><i style="width:14px;height:14px"></i>QELVARTIN BUILD</div>
  <div class="abs" style="left:60px;top:152px;font-size:9px;color:#fff;letter-spacing:1.6px">GRAPHICS WEB VIDEO CONSULTANTS</div>
  <h3>We Build Websites For The Non-Techie In Us All With Design. We Believe Good Design Can Solve Problems.</h3>
  <p>We help brands sell online with beautifully designed websites and effective digital marketing strategies that deliver results &amp; help your business grow.</p>
</section>

<!-- STEP CONNECTORS -->
<svg class="abs" style="left:300px;top:1570px" width="620" height="130" viewBox="0 0 620 130" fill="none" stroke="#b8a6cd" stroke-width="2">
  <path d="M305 0 V50 Q305 62 293 62 H45 Q31 62 31 76 V118"/>
  <path d="M313 0 V118" stroke="var(--lime)"/>
  <path d="M322 0 V50 Q322 62 334 62 H582 Q596 62 596 76 V118" stroke="var(--teal)"/>
  <circle cx="31" cy="123" r="5" fill="#b8a6cd" stroke="none"/>
  <circle cx="315" cy="123" r="5" fill="var(--lime)" stroke="none"/>
  <circle cx="596" cy="123" r="5" fill="var(--teal)" stroke="none"/>
</svg>

<div class="step" style="left:201px;top:1707px">
  <div class="ico" style="background:var(--lavender)">
    <svg width="40" height="40" viewBox="0 0 40 40" fill="none" stroke="#fff" stroke-width="1.6"><rect x="8" y="5" width="24" height="30" rx="2"/><rect x="12" y="11" width="4" height="4"/><rect x="12" y="18" width="4" height="4"/><rect x="12" y="25" width="4" height="4"/><path d="M19 13h9M19 20h9M19 27h9"/></svg>
  </div>
  <h4>TELL US YOUR NEEDS</h4>
  <p>Fill out our easy questionnaire so we can understand your problems.</p>
</div>
<div class="step" style="left:490px;top:1707px">
  <div class="ico" style="background:var(--lime)">
    <svg width="40" height="40" viewBox="0 0 40 40" fill="none" stroke="#fff" stroke-width="1.8"><path d="M12 7l4 7-3 3c2 4 5 7 9 9l3-3 7 4-2 5C19 32 8 21 8 9z"/></svg>
  </div>
  <h4>PHONE CALL</h4>
  <p>Book a time to have a chat in case we have more question about your goals.</p>
</div>
<div class="step" style="left:770px;top:1707px">
  <div class="ico" style="background:var(--teal)">
    <svg width="40" height="40" viewBox="0 0 40 40" fill="none" stroke="#fff" stroke-width="1.6"><rect x="5" y="7" width="24" height="10" rx="5"/><circle cx="10" cy="12" r="2"/><rect x="11" y="21" width="24" height="10" rx="5"/><circle cx="29" cy="26" r="4"/><path d="M27 26l1.5 1.5 2.5-3"/></svg>
  </div>
  <h4>CUSTOM QUOTE</h4>
  <p>Once we have made your plan, we'll get to work to build and launch your new website</p>
</div>

<!-- SERVICES -->
<section class="services">
  <svg class="abs" style="left:0;top:2009px" width="1200" height="643" viewBox="0 0 1200 643">
    <defs><linearGradient id="servGrad" x1="0" y1="0" x2="0" y2="1"><stop offset="0" stop-color="#b8a6cd"/><stop offset="1" stop-color="#7c58c8"/></linearGradient></defs>
    <path d="M540 10 C700 0 1000 -5 1200 0 V643 H455 C430 560 440 470 510 400 C590 320 580 260 560 170 C545 100 500 40 540 10Z" fill="url(#servGrad)"/>
  </svg>
  <h2>Services <b>We</b> <span>Provide</span></h2>
  <div class="rule" style="left:120px;top:2243px;width:70px"></div>
  <p>We Build Websites For The Non-Techie In Us All With Design. We Believe Good Design Can Solve Problems. We help brands sell online with beautifully designed websites and effective digital marketing strategies that deliver results &amp; help your business grow.</p>
  <div class="btn btn-lime" style="left:115px;top:2441px;width:174px;height:46px">Learn More</div>

  <div class="card card-white" style="left:832px;top:2063px;height:219px">
    <svg width="44" height="40" viewBox="0 0 44 40" fill="none" stroke="var(--teal)" stroke-width="1.6"><rect x="4" y="3" width="34" height="18"/><circle cx="11" cy="26" r="3"/><circle cx="21" cy="26" r="3"/><circle cx="31" cy="26" r="3"/><path d="M6 37c0-4 10-4 10 0M16 37c0-4 10-4 10 0M26 37c0-4 10-4 10 0"/></svg>
    <h5>Workshops</h5>
    <p>We offer workshops to business, schools, non-profits, and organizations. We can taylor the workshop to your organizations if needed.</p>
    <span class="mini" style="background:var(--lime);color:#fff">Learn More</span>
  </div>
  <div class="card card-teal" style="left:585px;top:2113px;height:224px">
    <svg width="44" height="40" viewBox="0 0 44 40" fill="none" stroke="#fff" stroke-width="1.6"><rect x="4" y="4" width="32" height="26"/><path d="M4 10h32"/><circle cx="26" cy="24" r="7"/><circle cx="26" cy="24" r="2.5"/></svg>
    <h5>Website<br>Maintenance</h5>
    <p>Want to keep your business growing? Your website is crucial to your growth and success. When operating seam-lessly with your goals.</p>
    <span class="mini" style="background:#fff;color:var(--teal)">Learn More</span>
  </div>
  <div class="card card-lime" style="left:830px;top:2311px;height:219px">
    <svg width="44" height="40" viewBox="0 0 44 40" fill="none" stroke="#fff" stroke-width="1.6"><rect x="10" y="8" width="18" height="18" transform="rotate(10 19 17)"/><circle cx="19" cy="17" r="5"/><path d="M30 6l8 8M4 34h30"/></svg>
    <h5>Logo Design</h5>
    <p>We create logos for all kinds of compa-nies and brands. A logo can be a name-plate or a monogram, emblem, symbol or signet. A logo can take a week or a year to develop.</p>
    <span class="mini" style="background:#fff;color:var(--lime)">Learn More</span>
  </div>
  <div class="card card-white" style="left:583px;top:2352px;height:219px">
    <svg width="44" height="40" viewBox="0 0 44 40" fill="none" stroke="var(--teal)" stroke-width="1.8"><path d="M8 4l28 30M36 4L8 34M6 36l4-4M38 36l-4-4"/></svg>
    <h5>Artist Website</h5>
    <p>When you are in the art world you need to show your craft to get exposure, gigs and sales. We love working with artists that value good design!</p>
    <span class="mini" style="background:var(--lime);color:#fff">Learn More</span>
  </div>
</section>

<!-- TESTIMONIALS -->
<section class="testi">
  <div class="abs" style="left:0;top:2652px;width:1200px;height:585px;background:var(--soft)"></div>
  <svg class="abs" style="left:0;top:2652px" width="620" height="585" viewBox="0 0 620 585">
    <path d="M0 0 H470 C380 60 370 140 470 240 C570 340 600 470 535 585 H0Z" fill="var(--peach)"/>
  </svg>
  <h2>Customer <span>Testimnials</span></h2>
  <div class="testi-card">
    <div class="testi-photo" role="img" aria-label="Photo: smiling client working at a laptop in an office">
      <div class="play"><svg width="20" height="20" viewBox="0 0 20 20"><path d="M6 3l11 7-11 7z" fill="#9a9aa6"/></svg></div>
      <div class="abs" style="left:200px;top:192px;color:#fff;font-size:11px;font-weight:600">PLAY VIDEO</div>
    </div>
    <h3>What Plumeravik Guides Experienced After Getting Certified</h3>
    <p>Working with Marin was easy and exciting. He was able to distill our ideas and keep us focused on what we needed for our website. He was able to speak to us in simple language on the details and operations of our website.</p>
    <div class="abs" role="img" aria-label="Client portrait" style="left:516px;top:234px;width:38px;height:38px;border-radius:50%;background:linear-gradient(135deg,#d7b49a,#8d6e5b)"></div>
    <div class="abs" style="left:568px;top:238px;font-size:10px;font-weight:700">DORIAN LESSA</div>
    <div class="abs" style="left:568px;top:252px;font-size:14px;color:#f3b321;letter-spacing:1px">★★★★★</div>
  </div>
  <svg class="abs" style="left:52px;top:2913px" width="36" height="60" viewBox="0 0 36 60" fill="none" stroke="#fff" stroke-width="2.5"><path d="M32 2L4 30l28 28"/></svg>
  <svg class="abs" style="left:1096px;top:2913px" width="36" height="60" viewBox="0 0 36 60" fill="none" stroke="#aaaab4" stroke-width="2.5"><path d="M4 2l28 28L4 58"/></svg>
</section>

<!-- PROJECTS -->
<section class="projects">
  <h2>OUR PROJECTS</h2>
  <div class="abs" style="left:242px;top:3414px;width:56px;height:3px;background:var(--lavender)"></div>
  <h3>The Valley Harbor Wellness Network</h3>
  <p>Lorem Ipsum is simply dummy text of the printing and typesetting indus-try. Lorem Ipsum has been</p>
  <div class="btn btn-lime" style="left:107px;top:3620px;width:150px;height:42px">View All</div>

  <div class="abs" style="left:535px;top:3281px;width:512px;height:512px;border-radius:50%;background:radial-gradient(circle,#fff 60%,#f7ebe5 100%)"></div>
  <div class="abs" style="left:551px;top:3297px;width:480px;height:480px;border-radius:50%;background:linear-gradient(180deg,#9c86cc,#b8a6cd 55%,#8a6fc6)"></div>
  <div class="abs" style="left:492px;top:3420px;width:90px;height:210px;background:#f7f7f9;border-radius:4px;box-shadow:0 6px 20px rgba(0,0,0,.08)"></div>
  <div class="abs" style="left:1000px;top:3420px;width:70px;height:210px;background:linear-gradient(#fff6ea,#f3d99c);border-radius:4px"></div>
  <div class="abs" style="left:580px;top:3389px;width:422px;height:266px;background:#fff;border:6px solid #e8e8ec;border-radius:10px"></div>
  <div class="abs" role="img" aria-label="Project website screenshot: living room interior banner" style="left:592px;top:3440px;width:398px;height:200px;background:linear-gradient(120deg,#c9c4bd,#7d7974 50%,#b0a89e)"></div>
  <div class="abs" style="left:530px;top:3655px;width:520px;height:12px;background:linear-gradient(#e6e6ea,#c9c9d0);border-radius:0 0 16px 16px"></div>
  <svg class="abs" style="left:760px;top:3706px" width="66" height="14" viewBox="0 0 66 14"><circle cx="7" cy="7" r="6" fill="#fff"/><circle cx="25" cy="7" r="6" fill="#d6cce6"/><circle cx="43" cy="7" r="6" fill="#d6cce6"/><circle cx="61" cy="7" r="5" fill="#d6cce6"/></svg>
</section>

<!-- QUOTE FORM -->
<section class="quote">
  <div class="quote-bg"></div>
  <div class="quote-card">
    <h2>REQUEST A FREE QUOTE</h2>
    <div class="abs" style="left:404px;top:84px;width:56px;height:3px;background:var(--lavender)"></div>
  </div>
  <div class="field" style="left:263px;top:4039px">First Name</div>
  <div class="field" style="left:611px;top:4039px">Last Name</div>
  <div class="field" style="left:263px;top:4100px">Phone</div>
  <div class="field" style="left:611px;top:4100px">Email</div>
  <div class="field" style="left:263px;top:4161px">Company Name</div>
  <div class="field" style="left:611px;top:4161px">Company Site</div>
  <div class="field msg" style="left:263px;top:4221px">Message</div>
  <div class="btn btn-teal" style="left:509px;top:4313px;width:185px;height:47px">Send Message</div>
</section>

<!-- FOOTER -->
<footer class="footer">
  <div class="vline" style="left:472px"></div>
  <div class="vline" style="left:754px"></div>
  <div class="vline" style="left:943px"></div>
  <div class="logo" style="left:152px;top:74px;font-size:30px"><i style="width:14px;height:14px"></i>QELVARTIN BUILD</div>
  <div class="abs" style="left:152px;top:116px;font-size:8px;letter-spacing:1.5px">GRAPHICS WEB VIDEO CONSULTANTS</div>
  <div class="small" style="left:152px;top:150px;font-size:9px;line-height:18px">Copyright 2021 Qelvartin Build All Right Reserved<br>Privacy Policy &nbsp;|&nbsp; Contact</div>

  <div class="divider" style="left:470px"></div>
  <h6 style="left:522px">CONTACT US</h6>
  <svg class="abs" style="left:522px;top:92px" width="16" height="20" viewBox="0 0 16 20" fill="none" stroke="#fff" stroke-width="1.6"><path d="M8 19s6-6.5 6-11A6 6 0 0 0 2 8c0 4.5 6 11 6 11z"/><circle cx="8" cy="8" r="2.2"/></svg>
  <div class="small" style="left:550px;top:92px">18 Larkspur Row, Ashbury<br>MA 01099</div>
  <svg class="abs" style="left:522px;top:152px" width="18" height="18" viewBox="0 0 18 18" fill="none" stroke="#fff" stroke-width="1.5"><path d="M5 2l2.5 4-1.5 1.5c1 2 2.5 3.5 4.5 4.5L12 10.5l4 2.5-1 2.5C9 15.5 2.5 9 2.5 3z"/></svg>
  <div class="small" style="left:550px;top:152px">1-413-555-0187</div>
  <svg class="abs" style="left:522px;top:190px" width="20" height="16" viewBox="0 0 20 16" fill="none" stroke="#fff" stroke-width="1.5"><rect x="1" y="2" width="18" height="12"/><path d="M1 2l9 7 9-7"/></svg>
  <div class="small" style="left:550px;top:189px">marin@tovarellaplexworks.com</div>

  <div class="divider" style="left:752px"></div>
  <h6 style="left:791px">NAVIGATE</h6>
  <div class="small" style="left:791px;top:92px">Home<br>Web<br>Print<br>Video</div>

  <div class="divider" style="left:941px"></div>
  <h6 style="left:982px">FOLLOW US</h6>
  <svg class="abs" style="left:982px;top:94px" width="84" height="24" viewBox="0 0 84 24"><circle cx="12" cy="12" r="11" fill="#fff"/><circle cx="40" cy="12" r="11" fill="#fff"/><circle cx="68" cy="12" r="11" fill="#fff"/></svg>
</footer>

</body>
</html>
```